Window film company looking for a visually appealing box design to ship out products with.

We need a new box design for our window film products. We will provide images of our previous box design as an example. The design we are looking for should have a bold and luxurious tone to it. Our Company name, "Halbrook Window Films," should also be easily showcased with an Emphasis on "Halbrook". We need to have an ulta modern techy vibe in the box design. We want to make sure its simple but has the blue pop. The designs we showed you are examples but i think they have to much going on and i want something more simple.

Target Market(s)

Window film Industry

Font styles to use
Other font styles liked:
• I want a font similar to the "vossen font" RED image below.

Requirements
Must have
• Company name : HALBROOK
WEBSITE: www.halbrookdistributors.com
Youtube: Halbrook
facebook:HalbrookDistribution
Instagram: HalbrookDistribution

COLOR CODE OF OUR BUSINESS : MUST MATCH THE BLUE IN OUR COMPANY LOGO. (HALBROOK DISTIBUTION)

RGB:
Red: 84
Green:200
blue:232
Nice to have
• I would need to have a modern look. More of a dark vibe.
Should not have
• Any other colors besides our company colors.

```html
<!DOCTYPE html>
<html lang="en">
<head>
<meta charset="utf-8">
<title>Halbrook Window Films – Box Wrap</title>
<link href="https://fonts.googleapis.com/css2?family=Michroma&display=swap" rel="stylesheet">
<style>
  :root {
    --brand-blue: #54c8e8;
    --brand-blue-soft: #6fd2ee;
    --page-bg: #9ae8fc;
    --ink: #1a1a1a;
    --panel-dark: #161616;
    --panel-mid: #2b2b2b;
    --line-white: #ffffff;
  }
  html, body {
    margin: 0;
    width: 1200px;
    height: 1200px;
    overflow: hidden;
    background: var(--page-bg);
  }
  .canvas {
    width: 1200px;
    height: 1200px;
    display: flex;
    align-items: center;
    justify-content: center;
  }
  .box-wrap {
    width: 1086px;
    height: 444px;
    display: block;
  }
  .wrap-text {
    font-family: "Michroma", sans-serif;
    font-weight: 400;
  }
  .text-blue { fill: var(--brand-blue); }
  .text-ink { fill: var(--ink); }
  .flap { fill: var(--brand-blue); }
  .band-fill { fill: url(#bandGradient); }
  .panel-fill { fill: url(#panelGradient); }
  .panel-base { fill: var(--panel-dark); }
  .banner { fill: var(--ink); }
  .rule { fill: none; stroke: var(--line-white); stroke-width: 9; stroke-linejoin: round; }
  .mark-square { fill: none; stroke: var(--brand-blue); stroke-width: 6; }
  .icon-square { fill: var(--ink); }
  .icon-circle { fill: none; stroke: var(--ink); stroke-width: 3; }
  .flap-divider { stroke: #2a2a2a; stroke-width: 2; }
</style>
</head>
<body>
<main class="canvas">
  <svg class="box-wrap" viewBox="0 0 1748 714" xmlns="http://www.w3.org/2000/svg" xmlns:xlink="http://www.w3.org/1999/xlink">
    <defs>
      <linearGradient id="panelGradient" x1="0" y1="0" x2="0" y2="1">
        <stop offset="0" stop-color="#262626"/>
        <stop offset="1" stop-color="#1a1a1a"/>
      </linearGradient>
      <linearGradient id="bandGradient" x1="0" y1="0" x2="1" y2="0">
        <stop offset="0" stop-color="#5ccbea"/>
        <stop offset="0.5" stop-color="#74d4ef"/>
        <stop offset="1" stop-color="#5ccbea"/>
      </linearGradient>

      <g id="sidePanel">
        <rect class="panel-base" x="238" y="478" width="1272" height="236"/>
        <rect class="panel-fill" x="238" y="478" width="1272" height="171" role="img" aria-label="Dark hexagon texture"/>
        <path class="rule" d="M238 566 H770 Q800 566 812 590 L826 624 Q838 649 868 649 H1510"/>
        <text class="wrap-text text-blue" x="293" y="652" font-size="56" textLength="485" lengthAdjust="spacingAndGlyphs">HALBROOK</text>
        <text class="wrap-text text-blue" x="778" y="684" font-size="22" text-anchor="end">WINDOW FILMS</text>
        <text class="wrap-text text-blue" x="980" y="694" font-size="17" textLength="480" lengthAdjust="spacingAndGlyphs">WWW.HALBROOKDISTRIBUTORS.COM</text>
      </g>
    </defs>

    <!-- end flaps -->
    <rect class="flap" x="0" y="0" width="1748" height="714"/>

    <!-- top side panel (inverted when flat) -->
    <use xlink:href="#sidePanel" transform="translate(1748 714) rotate(180)"/>

    <!-- lid band -->
    <rect class="band-fill" x="0" y="238" width="1748" height="240" role="img" aria-label="Light blue hexagon texture band"/>

    <!-- lid banner -->
    <polygon class="banner" points="50,280 850,280 888,358 850,436 50,436 18,358"/>
    <line class="flap-divider" x1="238" y1="280" x2="238" y2="436"/>
    <text class="wrap-text text-blue" x="128" y="364" font-size="13" text-anchor="middle">HALBROOK</text>

    <rect class="mark-square" x="326" y="306" width="100" height="100"/>
    <text class="wrap-text text-blue" x="470" y="360" font-size="36" textLength="345" lengthAdjust="spacingAndGlyphs">HALBROOK</text>
    <text class="wrap-text text-blue" x="496" y="386" font-size="17" textLength="294" lengthAdjust="spacingAndGlyphs">DISTRIBUTION</text>

    <!-- social handles -->
    <g class="social-list">
      <text class="wrap-text text-ink" x="1406" y="320" font-size="17" text-anchor="end">HALBROOK</text>
      <rect class="icon-square" x="1416" y="300" width="26" height="26" rx="4"/>
      <text class="wrap-text text-ink" x="1406" y="366" font-size="17" text-anchor="end">HALBROOKDISTRIBUTION</text>
      <rect class="icon-square" x="1416" y="346" width="26" height="26" rx="4"/>
      <text class="wrap-text text-ink" x="1406" y="412" font-size="17" text-anchor="end">HALBROOKDISTRIBUTION</text>
      <circle class="icon-circle" cx="1429" cy="405" r="12"/>
    </g>

    <!-- right tuck flap -->
    <text class="wrap-text text-ink" x="1628" y="364" font-size="13" text-anchor="middle">HALBROOK</text>

    <!-- bottom side panel -->
    <use xlink:href="#sidePanel"/>
  </svg>
</main>
</body>
</html>
```